Website Refresh

I'm looking to refresh my Squarespace website. www.brettmadeley.example

I am pretty happy with the content but would like a better navigation bar, livelier color choices, consistent type faces, and a more modern look. I am willing to pay extra to implement suggested improvements that would make the site more appealing

```html
<!DOCTYPE html>
<html lang="en">
<head>
<meta charset="utf-8">
<title>Summit Circle – Brett Madeley, Master Chair</title>
<link href="https://fonts.googleapis.com/css2?family=Space+Mono:wght@700&family=Open+Sans:wght@400;600;700&display=swap" rel="stylesheet">
<style>
:root{
  --navy:#0b3d63;
  --navy-dark:#072c49;
  --navy-deep:#05233b;
  --ink:#1d2a36;
  --muted:#6b7785;
  --line:#d9e0e7;
  --pale:#eef3f7;
  --white:#ffffff;
}
*{box-sizing:border-box;margin:0;padding:0}
html,body{width:1200px;height:4320px;overflow:hidden}
body{font-family:"Open Sans",Arial,sans-serif;color:var(--ink);background:var(--white);position:relative}
.head{font-family:"Space Mono","Courier New",monospace;font-weight:700;text-transform:uppercase;letter-spacing:2px}
.btn{position:absolute;background:var(--navy);color:var(--white);font-weight:700;font-size:15px;letter-spacing:1px;text-transform:uppercase;display:flex;align-items:center;justify-content:center;border-radius:3px;white-space:nowrap}
.photo{position:absolute}

/* header */
.site-header{position:absolute;left:0;top:0;width:1200px;height:132px;background:var(--white)}
.brand{position:absolute;left:40px;top:44px;font-size:22px;font-weight:700;color:var(--navy);letter-spacing:1px;white-space:nowrap}
.brand-sub{position:absolute;left:40px;top:76px;font-size:9px;color:var(--muted);white-space:nowrap}
.nav{position:absolute;left:256px;top:58px;display:flex;gap:22px;font-size:13px;font-weight:700;color:var(--ink);text-transform:uppercase;white-space:nowrap}
.site-header .btn{left:980px;top:44px;width:180px;height:46px;font-size:14px}

/* hero */
.hero{position:absolute;left:0;top:132px;width:1200px;height:620px;background:linear-gradient(90deg,#0c2840 0%,#3d5a72 55%,#8aa0b3 100%)}
.hero h1{position:absolute;left:112px;top:182px;font-size:44px;line-height:54px;color:var(--white);width:620px}
.hero p{position:absolute;left:112px;top:300px;width:420px;font-size:14px;line-height:22px;color:#dbe6ef}
.hero .btn{left:112px;top:388px;width:160px;height:40px;background:var(--white);color:var(--navy)}
.dots{position:absolute;display:flex;gap:8px}
.dots i{width:10px;height:10px;border-radius:50%;background:#b8c4cf;display:block}
.dots i.on{background:var(--white)}

/* about */
.title{position:absolute;left:0;width:1200px;text-align:center;font-size:28px;color:var(--ink)}
.tabs{position:absolute;left:0;top:900px;width:1200px;display:flex;justify-content:center;gap:52px;font-size:15px}
.tabs span{padding-bottom:6px}
.tabs .on{color:var(--navy);border-bottom:3px solid var(--navy)}
.frame{position:absolute;left:300px;top:966px;width:260px;height:290px;border:8px solid var(--navy)}
.values{position:absolute;left:602px;top:980px;width:410px}
.value{margin-bottom:22px;position:relative;padding-left:22px}
.value:before{content:"";position:absolute;left:0;top:5px;width:10px;height:10px;border-radius:50%;background:var(--navy)}
.value h4{font-size:14px;font-weight:700;letter-spacing:1px;color:var(--ink)}
.value p{font-size:13px;line-height:20px;color:var(--muted)}

/* testimonials */
.band{position:absolute;left:0;top:1398px;width:1200px;height:600px;background:var(--navy)}
.band .title{color:var(--white);top:92px}
.band p.lead{position:absolute;left:300px;top:150px;width:600px;text-align:center;color:#d5e2ed;font-size:15px;line-height:24px}
.video{position:absolute;left:265px;top:1632px;width:670px;height:360px;background:linear-gradient(135deg,#c7d1d8,#8f9ea9 60%,#5b6d7a)}
.video-logo{position:absolute;right:22px;top:18px;color:var(--navy);font-weight:700;font-size:24px}
.video-cap{position:absolute;left:24px;bottom:24px;color:var(--white);font-size:23px;white-space:nowrap}
.play{position:absolute;right:20px;bottom:24px;display:flex;align-items:center;gap:8px;color:var(--white);font-weight:700;font-size:14px;white-space:nowrap}
.arrow{position:absolute;width:26px;height:26px;border-radius:50%;background:var(--white);display:flex;align-items:center;justify-content:center}

/* reviews */
.card{position:absolute;top:2184px;width:400px;height:236px;background:var(--white);box-shadow:0 4px 18px rgba(10,40,70,.14);border-radius:4px;padding:26px 30px}
.card .avatar{position:absolute;left:30px;top:24px;width:52px;height:52px;border-radius:50%;background:#9aa8b4}
.card h5{margin-left:70px;font-size:13px;font-weight:700;letter-spacing:1px}
.card .role{margin-left:70px;font-size:11px;color:var(--muted)}
.card .stars{margin-left:70px;color:#f2b01e;font-size:12px;letter-spacing:2px}
.card p{margin-top:26px;font-size:13px;line-height:21px;color:var(--muted);font-style:italic}

/* team */
.team{position:absolute;left:0;top:2500px;width:1200px;height:690px;background:linear-gradient(180deg,#ffffff 0%,#f3f6f9 55%,#a9bfd2 100%)}
.team .quote{position:absolute;left:230px;top:130px;width:740px;text-align:center;font-size:15px;line-height:23px;font-weight:600;color:var(--ink)}
.member{position:absolute;top:240px;width:218px;text-align:center}
.member .pic{height:260px;background:linear-gradient(180deg,#b9c3cc,#6b7a88)}
.member h6{margin-top:12px;font-size:15px;font-weight:700;font-family:"Space Mono","Courier New",monospace}
.member span{font-size:11px;color:var(--muted)}
.team .btn{left:515px;top:614px;width:170px;height:42px;background:var(--white);color:var(--navy);border:2px solid var(--navy)}

/* chair */
.chair-frame{position:absolute;left:185px;top:3366px;width:345px;height:258px;border:8px solid var(--navy)}
.chair{position:absolute;left:580px;top:3376px;width:470px}
.chair h3{font-size:21px;color:var(--ink);white-space:nowrap;letter-spacing:1.5px}
.chair p{margin-top:16px;font-size:14px;line-height:23px;color:var(--muted);width:430px}
.chair .btn{position:relative;margin-top:22px;width:160px;height:40px}

/* newsletter */
.news{position:absolute;left:0;top:3810px;width:1200px;height:300px;background:var(--navy)}
.news .title{color:var(--white);top:72px;font-size:26px}
.news .sub{position:absolute;left:0;top:120px;width:1200px;text-align:center;color:#d5e2ed;font-size:14px;text-transform:uppercase;letter-spacing:1px}
.input{position:absolute;left:355px;top:168px;width:400px;height:56px;background:var(--white);border-radius:4px;padding:0 22px;display:flex;align-items:center;color:#8a96a2;font-size:15px}
.news .btn{left:780px;top:168px;width:160px;height:56px;background:var(--white);color:var(--navy)}

/* footer */
.foot{position:absolute;left:0;top:4110px;width:1200px;height:210px;background:var(--navy-deep)}
.foot .links{position:absolute;left:0;top:46px;width:1200px;display:flex;justify-content:center;gap:18px;color:var(--white);font-size:14px;font-weight:700;text-transform:uppercase;white-space:nowrap}
.foot .copy{position:absolute;left:0;top:98px;width:1200px;text-align:center;color:#a9bccc;font-size:12px}
.social{position:absolute;left:525px;top:138px;display:flex;gap:14px}
.social i{display:block;width:28px;height:28px;border-radius:50%;background:var(--white)}
</style>
</head>
<body>

<header class="site-header">
  <div class="brand">SUMMIT CIRCLE</div>
  <div class="brand-sub">Private advisory for chief executives</div>
  <nav class="nav"><span>Home</span><span>About Us</span><span>Testimonials</span><span>Success Stories</span><span>Brett's Blog</span><span>Brett Madeley Bio</span></nav>
  <div class="btn">Join the Group</div>
</header>

<section class="hero" role="img" aria-label="Executives seated around a boardroom table while the chair presents at a flip chart">
  <h1 class="head">Turning good CEO's into great CEO's</h1>
  <p>Our award winning CEO's will help you become a better leader making better decisions and getting better results for your company, family, and community.</p>
  <div class="btn">Contact Brett</div>
  <div class="dots" style="left:112px;top:484px"><i class="on"></i><i></i><i></i><i></i></div>
</section>

<h2 class="title head" style="top:836px">About the Group</h2>
<div class="tabs head"><span class="on">Group Values</span><span>Group Personality</span></div>
<div class="frame"></div>
<div class="photo" role="img" aria-label="Group photo of the members standing together indoors" style="left:280px;top:986px;width:262px;height:270px;background:linear-gradient(160deg,#7f8c97,#3f4e5b)"></div>
<div class="values">
  <div class="value"><h4>CARING:</h4><p>We care about each other and commit to each other's success.</p></div>
  <div class="value"><h4>CHALLENGE:</h4><p>We challenge each other on tough issues to help get past our own beliefs, thoughts and blind spots.</p></div>
  <div class="value"><h4>GROWTH:</h4><p>We are committed to at least double digit growth.</p></div>
  <div class="value"><h4>TRUST:</h4><p>We are trusting, open and respectful in this safe haven where we treat confidentiality as 100% given.</p></div>
</div>

<section class="band">
  <h2 class="title head">Member Video Testimonials</h2>
  <p class="lead">Our award winning CEO's will help you become a better leader making better decisions and getting better results for your company, family, and community.</p>
</section>
<div class="video" role="img" aria-label="Video still of a member speaking in her office">
  <div class="video-logo">SUMMIT CIRCLE</div>
  <div class="video-cap">Nora Whitfield, COO – Whitfield Homes</div>
  <div class="play"><svg width="26" height="26" viewBox="0 0 26 26"><circle cx="13" cy="13" r="12" fill="#fff"/><path d="M10 8l8 5-8 5z" fill="#0b3d63"/></svg>PLAY VIDEO</div>
</div>
<div class="arrow" style="left:218px;top:1774px"><svg width="10" height="10" viewBox="0 0 10 10"><path d="M7 1L3 5l4 4" stroke="#0b3d63" stroke-width="2" fill="none"/></svg></div>
<div class="arrow" style="left:956px;top:1774px"><svg width="10" height="10" viewBox="0 0 10 10"><path d="M3 1l4 4-4 4" stroke="#0b3d63" stroke-width="2" fill="none"/></svg></div>
<div class="dots" style="left:578px;top:2026px"><i style="background:#0b3d63"></i><i></i><i></i></div>

<h2 class="title head" style="top:2088px">Reviews</h2>
<div class="card" style="left:192px">
  <div class="avatar" role="img" aria-label="Reviewer portrait"></div>
  <h5>HOWARD PENROSE</h5><div class="role">President, Penrose Industrial Supply</div><div class="stars">★★★★★</div>
  <p>"There is no other environment like it where you can have others challenge your assumptions, ask you the tough questions, hold you accountable and be totally supportive and encouraging."</p>
</div>
<div class="card" style="left:612px">
  <div class="avatar" role="img" aria-label="Reviewer portrait"></div>
  <h5>RITA CALLOWAY</h5><div class="role">CEO, Calloway Logistics</div><div class="stars">★★★★★</div>
  <p>"Brett is one of my professional heroes. He not only helps me be the best I can be professionally, but he is my mentor to me, reminding me of what I am, why I do what I do and where I want to go."</p>
</div>
<div class="dots" style="left:578px;top:2474px"><i style="background:#0b3d63"></i><i style="background:#0b3d63"></i><i style="background:#0b3d63"></i></div>

<section class="team">
  <h2 class="title head" style="top:74px">Team Members</h2>
  <p class="quote">"Although we come from different places, we have much in common and so much to share. The group through its collective experience, trust and dynamic array of personalities provides each member with candid, practical and immediate feedback."</p>
  <div class="member" style="left:135px"><div class="pic" role="img" aria-label="Portrait of Lisa Marten"></div><h6>Lisa Marten, CEO</h6><span>Marten Business Services</span></div>
  <div class="member" style="left:370px"><div class="pic" role="img" aria-label="Portrait of Michael Strand"></div><h6>Michael Strand</h6><span>President &amp; Founder, Strand Partners</span></div>
  <div class="member" style="left:605px"><div class="pic" role="img" aria-label="Portrait of Asha Verma"></div><h6>Asha Verma</h6><span>President, Verma Group</span></div>
  <div class="member" style="left:840px"><div class="pic" role="img" aria-label="Portrait of Jeremy Holt"></div><h6>Jeremy Holt</h6><span>President, Holt Works</span></div>
  <div class="btn">Meet Our Team</div>
</section>

<div class="chair-frame"></div>
<div class="photo" role="img" aria-label="Portrait of Brett Madeley, master chair" style="left:200px;top:3382px;width:315px;height:226px;background:linear-gradient(180deg,#8c9aa6,#46566a)"></div>
<div class="chair">
  <h3 class="head">Brett Madeley, Master Chair</h3>
  <p>My purpose is to help You move from a good to great CEO, find your real purpose, and make a significant contribution to the world. It takes more than a snap of the finger for YOU to go from a good to great leader. And there's a big difference between leading and truly inspiring our team.</p>
  <p>I play many roles encouraging and empowering YOU to reach your highest potential by developing your ability to inspire, motivate and lead others to accomplish amazing results, and to create cultures of accountability, impact and respect.</p>
  <div class="btn">Contact Brett</div>
</div>

<section class="news">
  <h2 class="title head">Like to Know More?</h2>
  <div class="sub">Sign up for the newsletter and let's stay in touch.</div>
  <div class="input">Email Address</div>
  <div class="btn">Sign Up</div>
</section>

<footer class="foot">
  <div class="links"><span>Home</span><span>|</span><span>About Us</span><span>|</span><span>Testimonials</span><span>|</span><span>Success Stories</span><span>|</span><span>Brett's Blog</span><span>|</span><span>Brett Madeley Bio</span><span>|</span><span>Join the Group</span></div>
  <div class="copy">Copyright © 2022 Summit Circle. Private advisory board for CEO's executives &amp; business owners. All Rights Reserved.</div>
  <div class="social"><i></i><i></i><i></i><i></i></div>
</footer>

</body>
</html>
```